Property Developer - Simple yet Sophisticated and Sharp Business Card

We are a medium sized property developer involved mainly in townhouse developments and land subdivisions.

The company is looking for a simple, sharp and sophisticated business card that will be given to contractors, land owners, financiers etc and thus will need to look professional.

Property development related graphics and art can be used, however the card is not to be too "busy" or crowded. Our company name is KL Estates which could possibly be incorporated into the graphics or artwork.

Single sided and/or double sided designs will be acceptable.

A Simple, Sophisticated, Sharp design please!

Good Luck !

```html
<!DOCTYPE html>
<html lang="en">
<head>
<meta charset="utf-8">
<title>KL Estates – Business Card Set</title>
<link href="https://fonts.googleapis.com/css2?family=Montserrat:wght@800&family=Open+Sans:wght@300;400;600&display=swap" rel="stylesheet">
<style>
  :root {
    --brand-blue: #0896c5;
    --brand-blue-deep: #0a8dbb;
    --charcoal: #48484b;
    --paper: #ffffff;
    --text-dark: #3e3e40;
  }
  * { box-sizing: border-box; margin: 0; padding: 0; }
  html, body { width: 1200px; height: 689px; overflow: hidden; background: var(--paper); }
  .sheet { position: relative; width: 1200px; height: 689px; }

  .card { position: absolute; width: 584px; height: 331px; overflow: hidden; }
  .card--front-a { left: 13px; top: 9px; background: var(--brand-blue); }
  .card--back-a  { left: 606px; top: 9px; background: var(--paper); }
  .card--back-b  { left: 13px; top: 348px; background: var(--paper); }
  .card--front-b {
    left: 606px; top: 348px;
    background: radial-gradient(circle at 40% 45%, #16a4d2 0%, var(--brand-blue-deep) 70%);
  }

  .wordmark { position: absolute; display: flex; align-items: center; }
  .wordmark__dot { border-radius: 50%; flex: none; }
  .wordmark__name {
    font-family: 'Montserrat', sans-serif; font-weight: 800;
    letter-spacing: -0.5px; white-space: nowrap;
  }
  .card--front-a .wordmark, .card--front-b .wordmark { left: 44px; top: 124px; gap: 40px; }
  .card--front-b .wordmark { left: 48px; top: 128px; }
  .card--front-a .wordmark__dot, .card--front-b .wordmark__dot { width: 82px; height: 82px; background: var(--paper); }
  .card--front-a .wordmark__name, .card--front-b .wordmark__name { font-size: 40px; color: var(--paper); }

  .card--back-a .wordmark, .card--back-b .wordmark { left: 42px; top: 30px; gap: 26px; }
  .wordmark--small .wordmark__dot { width: 62px; height: 62px; background: var(--brand-blue); }
  .wordmark--small .wordmark__name { font-size: 29px; color: var(--charcoal); }

  .person { position: absolute; left: 0; top: 176px; width: 210px; }
  .person__name {
    font-family: 'Open Sans', sans-serif; font-weight: 300;
    font-size: 30px; line-height: 1; color: var(--brand-blue);
    text-align: right; padding-right: 6px; letter-spacing: -0.5px;
  }
  .person__role {
    margin-top: 3px; height: 12px; background: var(--charcoal);
    clip-path: polygon(0 0, 100% 0, 96% 100%, 0 100%);
    font-family: 'Open Sans', sans-serif; font-weight: 600;
    font-size: 9px; line-height: 12px; color: var(--paper);
    text-align: right; padding-right: 16px;
  }

  .contact-divider { position: absolute; left: 247px; top: 181px; width: 1px; height: 72px; background: #b9bcbf; }
  .contacts { position: absolute; left: 265px; top: 180px; list-style: none; }
  .contacts li {
    display: flex; align-items: center; gap: 8px; height: 19.3px;
    font-family: 'Open Sans', sans-serif; font-size: 12.5px; color: var(--text-dark);
  }
  .contacts svg { width: 14px; height: 12px; fill: var(--charcoal); flex: none; }

  .footer-band { position: absolute; left: 0; top: 291px; width: 100%; height: 27px; background: var(--charcoal); }
  .footer-band svg { position: absolute; left: 422px; top: 0; }
  .footer-strip { position: absolute; left: 0; top: 320px; width: 100%; height: 11px; background: var(--brand-blue); }
</style>
</head>
<body>
<main class="sheet">

  <section class="card card--front-a" aria-label="Card front">
    <div class="wordmark">
      <span class="wordmark__dot"></span>
      <span class="wordmark__name">KL ESTATES</span>
    </div>
  </section>

  <section class="card card--back-a" aria-label="Card back">
    <div class="wordmark wordmark--small">
      <span class="wordmark__dot"></span>
      <span class="wordmark__name">KL ESTATES</span>
    </div>
    <div class="person">
      <p class="person__name">DANIEL HART</p>
      <p class="person__role">GENERAL MANAGER</p>
    </div>
    <span class="contact-divider"></span>
    <ul class="contacts">
      <li><svg viewBox="0 0 14 12"><rect x="1" y="0" width="12" height="8" rx="1"/><rect x="0" y="9" width="14" height="3"/></svg>+ (07) 3250 6184</li>
      <li><svg viewBox="0 0 14 12"><rect x="3" y="0" width="8" height="3"/><rect x="0" y="4" width="14" height="5" rx="1"/><rect x="3" y="8" width="8" height="4"/></svg>+ (07) 3250 6190</li>
      <li><svg viewBox="0 0 14 12"><path d="M0 1h14v10H0z M1 2l6 5 6-5" fill="none" stroke="#48484b" stroke-width="1.5"/></svg>PROJECTS.KLESTATES@MAILBOX.COM</li>
      <li><svg viewBox="0 0 14 12"><path d="M7 0a4 4 0 0 1 4 4c0 3-4 8-4 8S3 7 3 4a4 4 0 0 1 4-4z"/></svg>PO BOX 2417 RIVERDALE NORTH QLD 4120</li>
    </ul>
    <div class="footer-band">
      <svg width="46" height="27" viewBox="0 0 46 27"><path d="M0 0h10l13 13.5L10 27H0l13-13.5z M20 0h10l13 13.5L30 27H20l13-13.5z" fill="#fff"/></svg>
    </div>
    <div class="footer-strip"></div>
  </section>

  <section class="card card--back-b" aria-label="Card back, alternate">
    <div class="wordmark wordmark--small">
      <span class="wordmark__dot"></span>
      <span class="wordmark__name">KL ESTATES</span>
    </div>
    <div class="person">
      <p class="person__name">DANIEL HART</p>
      <p class="person__role">GENERAL MANAGER</p>
    </div>
    <span class="contact-divider"></span>
    <ul class="contacts">
      <li><svg viewBox="0 0 14 12"><rect x="1" y="0" width="12" height="8" rx="1"/><rect x="0" y="9" width="14" height="3"/></svg>+ (07) 3250 6184</li>
      <li><svg viewBox="0 0 14 12"><rect x="3" y="0" width="8" height="3"/><rect x="0" y="4" width="14" height="5" rx="1"/><rect x="3" y="8" width="8" height="4"/></svg>+ (07) 3250 6190</li>
      <li><svg viewBox="0 0 14 12"><path d="M0 1h14v10H0z M1 2l6 5 6-5" fill="none" stroke="#48484b" stroke-width="1.5"/></svg>PROJECTS.KLESTATES@MAILBOX.COM</li>
      <li><svg viewBox="0 0 14 12"><path d="M7 0a4 4 0 0 1 4 4c0 3-4 8-4 8S3 7 3 4a4 4 0 0 1 4-4z"/></svg>PO BOX 2417 RIVERDALE NORTH QLD 4120</li>
    </ul>
    <div class="footer-band">
      <svg width="46" height="27" viewBox="0 0 46 27"><path d="M0 0h10l13 13.5L10 27H0l13-13.5z M20 0h10l13 13.5L30 27H20l13-13.5z" fill="#fff"/></svg>
    </div>
    <div class="footer-strip"></div>
  </section>

  <section class="card card--front-b" aria-label="Card front, alternate">
    <div class="wordmark">
      <span class="wordmark__dot"></span>
      <span class="wordmark__name">KL ESTATES</span>
    </div>
  </section>

</main>
</body>
</html>
```